Flyer to Promote Membership in a Trade Association

UPDATE: I am looking for something modern and clean. NO CLIP ART. Not flashy. Just professional and modern. For everyone looking at our current flyer, we don't like it. That's why we aer looking for a new one. So please don't replicate it or use it as inspiration.

I need a flyer to promote membership in the Durable Residence Backers League. It can (probably should) be 2-sided. The content is attached as well as our logo and brand guidelines.

```html
<!DOCTYPE html>
<html lang="en">
<head>
<meta charset="utf-8">
<title>Durable Residence Backers League – Membership Flyer</title>
<link rel="stylesheet" href="https://fonts.googleapis.com/css2?family=Libre+Baskerville:wght@700&family=Oswald:wght@500;600&family=Poppins:wght@400;500;600;700&display=swap">
<style>
:root{
  --orange:#f27c2f;
  --slate:#666c74;
  --dark:#3e434a;
  --ink:#2f3338;
  --text:#484d54;
  --mid:#7a8088;
  --muted:#8f959c;
  --light:#d9dce0;
  --panel:#e9ebee;
  --paper:#ffffff;
  --stage:#e2e4e7;
}
*{margin:0;padding:0;box-sizing:border-box}
html,body{width:1200px;height:2400px;overflow:hidden;background:var(--stage);font-family:"Poppins",sans-serif;color:var(--text)}
.flyer{position:absolute;left:150px;width:900px;height:1140px;background:var(--paper);overflow:hidden;box-shadow:0 6px 18px rgba(0,0,0,.18)}
.flyer-front{top:30px}
.flyer-back{top:1230px}
.abs{position:absolute}

/* brand */
.brand{display:flex;align-items:center;gap:14px}
.brand-mark{background:var(--orange);display:block}
.brand-name{font-family:"Poppins",sans-serif;font-weight:700;color:var(--slate);letter-spacing:-1px;line-height:1}
.brand-front{left:48px;top:56px}
.brand-front .brand-mark{width:58px;height:58px}
.brand-front .brand-name{font-size:66px}
.brand-back{left:566px;top:1002px}
.brand-back .brand-name{font-size:52px}
.brand-back .brand-mark{width:46px;height:46px}

/* front header */
.title-band{left:0;top:161px;width:521px;height:167px;background:var(--slate)}
.title-band h1{position:absolute;left:51px;top:24px;font-family:"Libre Baskerville",serif;font-weight:700;font-size:35px;line-height:40px;color:#fff;letter-spacing:.6px;text-transform:uppercase}
.tagline-band{left:0;top:328px;width:484px;height:108px;background:var(--orange);clip-path:polygon(0 0,100% 0,435px 100%,0 100%)}
.tagline-band h2{position:absolute;left:51px;top:14px;font-size:22px;line-height:27px;font-weight:700;color:#fff}
.tagline-band p{position:absolute;left:51px;top:74px;font-size:14px;color:#fff}

.hero-art{left:0;top:0;width:900px;height:1140px;pointer-events:none}

.intro{left:51px;top:476px;width:385px;font-size:14.5px;line-height:17.8px}

.section-title{left:53px;top:598px;font-size:28px;font-weight:700;color:var(--text)}
.activity{width:116px;text-align:center;font-size:14.5px;line-height:17.8px;color:var(--ink)}
.activity svg{display:block;margin:0 auto 8px}
.activity b{font-weight:600;display:block}
.rule-v{width:1px;background:#d0d3d7}

.access{left:53px;top:826px}
.access h2{font-size:31px;line-height:36px;font-weight:700;color:var(--orange)}
.access p{font-size:22px;line-height:26px;color:var(--ink);margin-top:2px}

.contact-title{left:53px;top:1018px;font-size:29px;font-weight:700;color:var(--orange)}
.phone{left:55px;top:1058px;display:flex;align-items:center;gap:15px}
.phone-number{font-family:"Oswald",sans-serif;font-weight:500;font-size:44px;line-height:56px;color:var(--ink)}
.ready{left:388px;top:1076px;font-size:25px;font-weight:700;color:var(--orange)}
.url{left:587px;top:1078px;width:254px;height:36px;background:var(--dark);color:#fff;font-weight:600;font-size:24px;letter-spacing:2.4px;text-align:center;line-height:36px}

/* tags */
.tag{display:block;position:relative;padding-bottom:10px}
.tag span{display:block;background:var(--orange);color:#fff;font-weight:700;font-size:20px;height:36px;line-height:36px;padding-left:14px;clip-path:polygon(0 0,100% 0,calc(100% - 24px) 100%,0 100%)}
.tag::after{content:"";position:absolute;left:40px;right:40px;bottom:2px;height:4px;background:linear-gradient(90deg,rgba(0,0,0,0),rgba(0,0,0,.16),rgba(0,0,0,0));border-radius:50%}
.tag.tag-dark span{background:var(--dark);height:54px;line-height:22px;padding-top:6px;font-size:20px}
.tag.tag-dark small{display:block;font-size:12.5px;letter-spacing:2.4px;font-weight:600;line-height:16px}

.join{left:392px;top:831px;width:253px}
.join span{font-size:23px}
.member-type{width:255px}
.member-type h3{font-size:17px;font-weight:700;color:var(--ink)}
.member-type p{font-size:17px;line-height:21px;color:var(--muted)}
.price{height:68px;border-radius:5px;text-align:center;font-family:"Oswald",sans-serif;font-weight:500;font-size:20px;line-height:26px;padding-top:14px;color:var(--ink);background:var(--light)}
.price small{display:block;font-family:"Poppins",sans-serif;font-size:11px;line-height:13px;font-weight:400}
.price.price-alt{background:var(--muted);color:#fff}

/* back */
.benefits-band{left:0;top:0;width:900px;height:153px}
.benefits-band h1{position:absolute;left:50px;top:50px;font-family:"Libre Baskerville",serif;font-weight:700;font-size:37px;line-height:40px;color:#fff;letter-spacing:.6px}
.benefit{width:366px}
.benefit .tag{width:350px}
.benefit p{font-size:17px;line-height:21px;color:var(--ink);margin-top:4px}
.benefit p b{font-weight:600}

.members-tab{left:50px;top:707px;width:396px;height:42px;background:var(--orange);border-radius:12px 12px 0 0;color:#fff;font-weight:700;font-size:16px;letter-spacing:3.4px;line-height:44px;padding-left:14px}
.members-panel{left:50px;top:746px;width:805px;height:236px;background:var(--panel);border-top:4px solid var(--orange);border-radius:0 0 12px 12px;display:grid;grid-template-columns:repeat(7,1fr);grid-template-rows:repeat(4,1fr);padding:8px 8px;align-items:center;justify-items:center}
.member-name{font-size:11.5px;font-weight:600;color:var(--text);text-align:center;line-height:13px}
</style>
</head>
<body>

<!-- FRONT -->
<section class="flyer flyer-front">
  <div class="brand brand-front abs">
    <span class="brand-mark"></span>
    <span class="brand-name">DRBL</span>
  </div>

  <div class="title-band abs">
    <h1>Durable<br>Residence Backers<br>League</h1>
  </div>
  <div class="tagline-band abs">
    <h2>Where LIHTC Investing<br>Excellence Begins</h2>
    <p>The Only Community Built Exclusively for Investors</p>
  </div>

  <svg class="hero-art abs" viewBox="0 0 900 1140">
    <defs>
      <linearGradient id="photoTone" x1="0" y1="0" x2="1" y2="1">
        <stop offset="0" stop-color="#3d4248"/>
        <stop offset=".55" stop-color="#9aa0a6"/>
        <stop offset="1" stop-color="#d7dade"/>
      </linearGradient>
    </defs>
    <polygon points="720,10 906,117.5 906,332.5 720,440 534,332.5 534,117.5" fill="none" stroke="var(--orange)" stroke-width="18"/>
    <polygon points="520,250 548,250 548,262 520,262" fill="var(--orange)"/>
    <polygon points="520,274 548,274 548,286 520,286" fill="var(--orange)"/>
    <polygon points="520,298 548,298 548,310 520,310" fill="var(--orange)"/>
    <polygon role="img" aria-label="Black-and-white photo of two business people shaking hands over a small model house" points="712,65 864,152.5 864,327.5 712,415 560,327.5 560,152.5" fill="url(#photoTone)"/>

    <polygon points="770,346 873,405.5 873,524.5 770,584 667,524.5 667,405.5" fill="none" stroke="var(--orange)" stroke-width="5"/>
    <polygon points="770,358 863,411.5 863,518.5 770,572 677,518.5 677,411.5" fill="#4c5259"/>
    <g fill="none" stroke="#fff" stroke-width="2">
      <circle cx="756" cy="404" r="7"/><circle cx="784" cy="404" r="7"/><circle cx="770" cy="424" r="7"/>
    </g>
    <text x="770" y="480" text-anchor="middle" font-family="Oswald,sans-serif" font-weight="600" font-size="42" fill="var(--orange)">60+</text>
    <text x="770" y="510" text-anchor="middle" font-family="Poppins,sans-serif" font-weight="700" font-size="22" fill="#fff">INVESTOR</text>
    <text x="770" y="537" text-anchor="middle" font-family="Poppins,sans-serif" font-weight="700" font-size="22" fill="#fff">FIRMS</text>

    <polygon points="567,388 660,441.5 660,548.5 567,602 474,548.5 474,441.5" fill="#767c84"/>
    <g fill="none" stroke="#fff" stroke-width="2">
      <circle cx="567" cy="450" r="13"/>
      <polyline points="561,450 566,455 574,445"/>
    </g>
    <text x="567" y="517" text-anchor="middle" font-family="Oswald,sans-serif" font-weight="600" font-size="40" fill="#fff">30 YEARS</text>
    <text x="567" y="551" text-anchor="middle" font-family="Oswald,sans-serif" font-weight="600" font-size="26" fill="var(--ink)">OF IMPACT</text>

    <polygon points="702,550 795,603.5 795,710.5 702,764 609,710.5 609,603.5" fill="#9ba1a8"/>
    <g fill="none" stroke="#fff" stroke-width="2">
      <circle cx="688" cy="596" r="6"/><circle cx="702" cy="592" r="6"/><circle cx="716" cy="596" r="6"/>
      <circle cx="702" cy="614" r="8"/>
    </g>
    <text x="702" y="675" text-anchor="middle" font-family="Oswald,sans-serif" font-weight="600" font-size="44" fill="var(--ink)">1,000+</text>
    <text x="702" y="698" text-anchor="middle" font-family="Poppins,sans-serif" font-weight="700" font-size="18" fill="#fff">INDUSTRY</text>
    <text x="702" y="719" text-anchor="middle" font-family="Poppins,sans-serif" font-weight="700" font-size="17" fill="#fff">PROFESSIONALS</text>
  </svg>

  <p class="intro abs">DRBL is where federal housing credit investors connect, learn, and lead. We are the only organization solely dedicated to LIHTC investors—giving you a trusted peer network, industry-setting standards, and the insights to stay informed.</p>

  <h2 class="section-title abs">WHAT MEMBERS DO</h2>

  <div class="activity abs" style="left:30px;top:650px">
    <svg width="50" height="50" viewBox="0 0 50 50"><polygon points="25,2 45,13.5 45,36.5 25,48 5,36.5 5,13.5" fill="var(--orange)"/><g stroke="#fff" stroke-width="1.6" fill="#fff"><line x1="17" y1="19" x2="33" y2="31"/><line x1="33" y1="19" x2="17" y2="31"/><circle cx="17" cy="19" r="2.5"/><circle cx="33" cy="19" r="2.5"/><circle cx="17" cy="31" r="2.5"/><circle cx="33" cy="31" r="2.5"/><circle cx="25" cy="25" r="3"/></g></svg>
    <b>Network</b>Peer<br>Groups &amp;<br>Forums
  </div>
  <div class="rule-v abs" style="left:139px;top:657px;height:135px"></div>
  <div class="activity abs" style="left:142px;top:650px">
    <svg width="50" height="50" viewBox="0 0 50 50"><polygon points="25,2 45,13.5 45,36.5 25,48 5,36.5 5,13.5" fill="var(--orange)"/><g stroke="#fff" stroke-width="1.8" fill="none"><circle cx="25" cy="22" r="7"/><line x1="22" y1="32" x2="28" y2="32"/><line x1="22.5" y1="35" x2="27.5" y2="35"/></g></svg>
    <b>Learn</b>Conferences<br>&amp; Webinar
  </div>
  <div class="rule-v abs" style="left:258px;top:657px;height:135px"></div>
  <div class="activity abs" style="left:251px;top:650px">
    <svg width="50" height="50" viewBox="0 0 50 50"><polygon points="25,2 45,13.5 45,36.5 25,48 5,36.5 5,13.5" fill="var(--orange)"/><g stroke="#fff" stroke-width="1.8" fill="none"><circle cx="31" cy="17" r="3"/><circle cx="18" cy="25" r="3"/><circle cx="31" cy="33" r="3"/><line x1="21" y1="23.5" x2="28.5" y2="18.5"/><line x1="21" y1="26.5" x2="28.5" y2="31.5"/></g></svg>
    <b>Share</b>Candid<br>Investor<br>Exchange
  </div>
  <div class="rule-v abs" style="left:368px;top:657px;height:135px"></div>
  <div class="activity abs" style="left:355px;top:650px">
    <svg width="50" height="50" viewBox="0 0 50 50"><polygon points="25,2 45,13.5 45,36.5 25,48 5,36.5 5,13.5" fill="var(--orange)"/><g stroke="#fff" stroke-width="1.8" fill="none"><rect x="16" y="16" width="18" height="18"/><line x1="16" y1="25" x2="34" y2="25"/><line x1="25" y1="16" x2="25" y2="34"/></g></svg>
    <b>Shape</b>Standards<br>&amp; Best<br>Practices
  </div>
  <div class="rule-v abs" style="left:474px;top:657px;height:135px"></div>
  <div class="activity abs" style="left:480px;top:650px">
    <svg width="50" height="50" viewBox="0 0 50 50"><polygon points="25,2 45,13.5 45,36.5 25,48 5,36.5 5,13.5" fill="var(--orange)"/><g fill="#fff"><rect x="15" y="28" width="4" height="7"/><rect x="21" y="24" width="4" height="11"/><rect x="27" y="20" width="4" height="15"/><rect x="33" y="15" width="4" height="20"/></g></svg>
    <b>Grow</b>Professional<br>Development
  </div>

  <div class="access abs">
    <h2>One membership,<br>unlimited access.</h2>
    <p>Your entire team can<br>participate<br>in DRBL activities.</p>
  </div>

  <h3 class="tag join abs"><span>Join DRBL Today</span></h3>

  <div class="member-type abs" style="left:393px;top:880px">
    <h3>Investor Members</h3>
    <p>Banks, Insurance<br>Companies, Economic<br>Investors</p>
  </div>
  <div class="rule-v abs" style="left:664px;top:872px;height:162px"></div>
  <div class="member-type abs" style="left:683px;top:880px;width:190px">
    <h3>Affiliate Members</h3>
    <p>Syndicators &amp;<br>Brokers</p>
  </div>

  <div class="price abs" style="left:393px;top:976px;width:128px">$5,000/YEAR<small>(assets ≥$5B)</small></div>
  <div class="price price-alt abs" style="left:525px;top:976px;width:120px">$1,000/YEAR<small>(assets &lt;$5B)</small></div>
  <div class="price abs" style="left:683px;top:972px;width:129px;padding-top:20px">$4,500/YEAR</div>

  <h2 class="contact-title abs">Contact Us</h2>
  <div class="phone abs">
    <svg width="42" height="42" viewBox="0 0 42 42" aria-hidden="true"><circle cx="21" cy="21" r="21" fill="var(--orange)"/><path d="M14 12c1-1 2.5-1 3.3 0l2 2.6c.7.9.6 2.1-.2 2.8l-1.3 1.2c.9 2 2.6 3.8 4.6 4.8l1.2-1.3c.8-.8 2-.9 2.8-.2l2.6 2c1 .8 1 2.3 0 3.3l-1.4 1.4c-1 1-2.6 1.3-4 .7-5-2-9-6-11-11-.6-1.4-.3-3 .7-4z" fill="#fff"/></svg>
    <span class="phone-number">555 0142 7788</span>
  </div>
  <p class="ready abs">Ready to join?</p>
  <p class="url abs">www.drbl.org</p>
</section>

<!-- BACK -->
<section class="flyer flyer-back">
  <div class="benefits-band abs" role="img" aria-label="Muted grey photo of a modern office building facade">
    <svg width="900" height="153" viewBox="0 0 900 153" style="position:absolute;left:0;top:0">
      <defs>
        <linearGradient id="bandTone" x1="0" y1="0" x2="1" y2="0">
          <stop offset="0" stop-color="#5d636b"/>
          <stop offset=".6" stop-color="#7a8088"/>
          <stop offset="1" stop-color="#8d939a"/>
        </linearGradient>
      </defs>
      <rect width="900" height="153" fill="url(#bandTone)"/>
      <polygon points="527,0 680,0 690,150 650,150" fill="#fff"/>
      <polygon points="757,0 822,0 822,92 757,118" fill="#fff"/>
      <polygon points="842,0 873,0 873,30 842,70" fill="#fff"/>
    </svg>
    <h1>MEMBER<br>BENEFITS</h1>
  </div>

  <div class="benefit abs" style="left:50px;top:185px">
    <h3 class="tag"><span>Members-Only Conferences</span></h3>
    <p>Two annual in-person meetings.<br><b>Spring Meeting:</b> investors-only for candid peer conversations.<br><b>Fall Summit:</b> full ecosystem gathering with syndicators and brokers.</p>
  </div>
  <div class="benefit abs" style="left:50px;top:365px">
    <h3 class="tag"><span>Live &amp; On-Demand Webinars</span></h3>
    <p>Free monthly Third Thursday webinars covering Year 15 issues, secondary transactions, securitizing developer fees and other emerging topics.</p>
  </div>
  <div class="benefit abs" style="left:50px;top:535px">
    <h3 class="tag tag-dark"><span>Shape Industry Standards<small>[INVESTOR ONLY]</small></span></h3>
    <p>DRBL's underwriting and asset management standards are adopted industry-wide. Influence them through our committees.</p>
  </div>

  <div class="benefit abs" style="left:483px;top:185px">
    <h3 class="tag"><span>Investor-Only Forums</span></h3>
    <p>Exclusive meetings and webinars for investors only, enabling candid conversations and meaningful collaboration.</p>
  </div>
  <div class="benefit abs" style="left:483px;top:339px">
    <h3 class="tag"><span>Peer-to-Peer Meetups</span></h3>
    <p>Find your peers—underwriters, asset managers, credit officers and more—with our meetups.</p>
  </div>
  <div class="benefit abs" style="left:483px;top:468px">
    <h3 class="tag"><span>Searchable Member Directory</span></h3>
    <p>Find underwriters, asset managers, and credit officers—searchable by role, firm type, and investment approach.</p>
  </div>
  <div class="benefit abs" style="left:486px;top:600px">
    <h3 class="tag tag-dark"><span>Emerging Leaders Program<small>[INVESTOR ONLY]</small></span></h3>
    <p>Develop your firm's next-generation leaders through dedicated professional development programming.</p>
  </div>

  <div class="members-tab abs">OUR INVESTOR MEMBERS INCLUDE</div>
  <div class="members-panel abs">
    <span class="member-name">Pellworth Health<br>Brimcove Care</span>
    <span class="member-name">Tandrel<br>Finance</span>
    <span class="member-name">Corvanti<br>Card Co.</span>
    <span class="member-name">Plumridge<br>Bancorp</span>
    <span class="member-name">Halvane<br>Trust</span>
    <span class="member-name">Orrindale<br>Capital</span>
    <span class="member-name">Ketterby<br>Bank</span>

    <span class="member-name">Marlowe Ferris<br>Bank</span>
    <span class="member-name">Quenby<br>Savings</span>
    <span class="member-name">Dunmere<br>Bank</span>
    <span class="member-name">Ashgrove<br>Lending</span>
    <span class="member-name">Vellacott<br>Partners</span>
    <span class="member-name">Brisbrook<br>Trust</span>
    <span class="member-name">Corlan Valley<br>Bank</span>

    <span class="member-name">Fenwright<br>Advisors</span>
    <span class="member-name">Hollisfield<br>Mutual</span>
    <span class="member-name">Pennacre<br>Bank</span>
    <span class="member-name">Zeltmar<br>Group</span>
    <span class="member-name">Tarnwell<br>Realty</span>
    <span class="member-name">Odell Kinsey<br>&amp; Co.</span>
    <span class="member-name">Saltmarsh<br>Bank</span>

    <span class="member-name">Brackenhurst<br>Assn</span>
    <span class="member-name">Aldwyck<br>Capital</span>
    <span class="member-name">Greyloft<br>Life</span>
    <span class="member-name">Wrenford<br>Bank</span>
    <span class="member-name">Moorvale<br>Financial</span>
    <span class="member-name">Cassivane<br>Bank</span>
    <span class="member-name">Ploverton<br>Coatings</span>
  </div>

  <div class="brand brand-back abs">
    <span class="brand-mark"></span>
    <span class="brand-name">DRBL</span>
  </div>

  <h2 class="contact-title abs">Contact Us</h2>
  <div class="phone abs">
    <svg width="42" height="42" viewBox="0 0 42 42" aria-hidden="true"><circle cx="21" cy="21" r="21" fill="var(--orange)"/><path d="M14 12c1-1 2.5-1 3.3 0l2 2.6c.7.9.6 2.1-.2 2.8l-1.3 1.2c.9 2 2.6 3.8 4.6 4.8l1.2-1.3c.8-.8 2-.9 2.8-.2l2.6 2c1 .8 1 2.3 0 3.3l-1.4 1.4c-1 1-2.6 1.3-4 .7-5-2-9-6-11-11-.6-1.4-.3-3 .7-4z" fill="#fff"/></svg>
    <span class="phone-number">555 0142 7788</span>
  </div>
  <p class="ready abs">Ready to join?</p>
  <p class="url abs">www.drbl.org</p>
</section>

</body>
</html>
```